First and Only Single Serving Dental Tooth Powder Company NEEDS Packaging DESIGN

We need a packaging design for a new company based in Florida called 'ZunoDab'. We created the first and only single serving dental tooth powder, for use with or without water. This solves a world problem in numerous faucets. Our product is great for Travelers, Adventure Seekers, Military Personnel, Daily Commuters and any one else wanting the cleanest mouth and freshest breath.

- This is a front and back of a 4(four) by 6(six) package design needed

Target Market(s)

Travelers,Outdoorsman, Adventure seekers, Daily Commuters, and Military Personnel.

Industry/Entity Type

Dental

Requirements
Must have
• -This must fit a package with the dimensions of 4" x 6"
• -four inches by six inches.
• -Earthy/Naturalistic Appeal
• - This is a front and back of a 4(four) by 6(six) package design needed
• -The package will be a White Nylon/Mylar bag
Nice to have
• -Clean your teeth anywhere, anytime...
• -Simple, Convenient, Effective
• -ZunoDab activates without water
• -Proudly made in the USA.
• -Package contains 15 ZunoDab's.
• -The Flavor for the ZunoDab is "Velmo Plum"
• -ZunoDab is for the everyday person on-the-go.
• -Our Story..
• Zunodab was brought to life for moments when time is vital and packing light is a must. We were tired of the same old ordinary way of cleaning our teeth while outdoors, on our adventures, or traveling the globe. The old way required water for it's use which isn't always readily available. With ZunoDab, water is not necessary. The package you hold in your hand contains no ordinary product. In fact, the way you use it is extremely unique and simple.
• Directions: Rip, Pour, Swish, Dispense. Enjoy your adventure responsibly!
Should not have
• A bunch of clutter besides that I am open to ideas.

```html
<!DOCTYPE html>
<html lang="en">
<head>
<meta charset="utf-8">
<title>ZunoDab Dental Tooth Powder – Pouch Front</title>
<link href="https://fonts.googleapis.com/css2?family=Quicksand:wght@300;400;500;700&family=Poppins:wght@600;700&display=swap" rel="stylesheet">
<style>
  :root {
    --backdrop: #e6e6e6;
    --pouch: #ffffff;
    --pouch-edge: #d9d9d9;
    --seal-line: #eeeeee;
    --brand-green: #1e6b35;
    --badge-green: #18502b;
    --amber: #e19a1c;
    --amber-deep: #d08410;
    --ink: #3a3a3a;
    --icon-line: #5a5a5a;
    --flavor: #b3124f;
    --on-dark: #ffffff;
  }
  * { margin: 0; padding: 0; box-sizing: border-box; }
  html, body {
    width: 1200px; height: 1000px; overflow: hidden;
    background: var(--backdrop);
  }
  .canvas { position: relative; width: 1200px; height: 1000px; }

  .pouch {
    position: absolute; left: 358px; top: 122px;
    width: 467px; height: 768px;
    background: var(--pouch);
    border: 1px solid var(--pouch-edge);
    border-radius: 24px 24px 8px 8px;
  }
  .pouch__seal {
    position: absolute; left: 0; right: 0; top: 66px;
    border-top: 1px solid var(--seal-line);
  }

  .brand {
    position: absolute; right: 22px; top: 144px;
    display: flex; align-items: center; gap: 8px;
  }
  .brand__dot {
    width: 20px; height: 20px; border-radius: 50%;
    background: var(--brand-green);
  }
  .brand__name {
    font-family: "Quicksand", sans-serif; font-weight: 700;
    font-size: 30px; color: var(--brand-green); letter-spacing: 0.5px;
  }

  .title { position: absolute; left: 48px; top: 212px; color: var(--amber); }
  .title__category {
    display: block;
    font-family: "Quicksand", sans-serif; font-weight: 300;
    font-size: 44px; letter-spacing: 0.6em; line-height: 1.1;
  }
  .title__product {
    display: block; margin-top: 4px;
    font-family: "Quicksand", sans-serif; font-weight: 400;
    font-size: 42px; line-height: 1.1; color: var(--amber-deep);
  }
  .title__product strong {
    font-family: "Poppins", sans-serif; font-weight: 700;
  }

  .features { position: absolute; left: 52px; top: 347px; list-style: none; }
  .feature {
    display: flex; align-items: center; gap: 11px;
    height: 46px; margin-bottom: 20px;
    font-family: "Quicksand", sans-serif; font-weight: 500;
    font-size: 12.5px; color: var(--ink);
  }
  .feature__icon { width: 46px; height: 46px; flex: none; }

  .count-badge {
    position: absolute; left: 84px; top: 655px;
    width: 68px; height: 68px; border-radius: 50%;
    background: var(--badge-green); color: var(--on-dark);
    display: flex; align-items: center; justify-content: center;
    font-family: "Poppins", sans-serif; font-weight: 700; font-size: 12.5px;
  }
  .flavor-band {
    position: absolute; left: 54px; top: 727px;
    width: 140px; height: 32px;
    background: var(--flavor); color: var(--on-dark);
    display: flex; align-items: center; justify-content: center;
    font-family: "Poppins", sans-serif; font-weight: 600; font-size: 12px;
    transform: rotate(1deg);
  }
  .sparkles { position: absolute; left: 270px; top: 618px; width: 190px; height: 150px; }
</style>
</head>
<body>
<main class="canvas">
  <section class="pouch" aria-label="ZunoDab tooth powder pouch, front">
    <div class="pouch__seal"></div>

    <div class="brand">
      <span class="brand__dot"></span>
      <span class="brand__name">ZunoDab</span>
    </div>

    <h1 class="title">
      <span class="title__category">Dental</span>
      <span class="title__product">Tooth <strong>Powder</strong></span>
    </h1>

    <ul class="features">
      <li class="feature">
        <svg class="feature__icon" viewBox="0 0 46 46" fill="none" stroke="var(--icon-line)" stroke-width="1.2">
          <circle cx="23" cy="23" r="21.5"/>
          <path d="M23 11 C19 18 16 22 16 27 a7 7 0 0 0 14 0 C30 22 27 18 23 11 Z"/>
          <line x1="14" y1="34" x2="32" y2="12"/>
        </svg>
        <span>Activates without water</span>
      </li>
      <li class="feature">
        <svg class="feature__icon" viewBox="0 0 46 46" fill="none" stroke="var(--icon-line)" stroke-width="1.2">
          <path d="M40 14 A20 20 0 1 0 42 28"/>
          <path d="M4 30 l-2 5 M4 30 l5 1"/>
          <text x="23" y="26" text-anchor="middle" font-family="Quicksand, sans-serif" font-size="9" font-weight="700" fill="var(--ink)" stroke="none">24/7</text>
        </svg>
        <span>Everyday,anywhere...</span>
      </li>
      <li class="feature">
        <svg class="feature__icon" viewBox="0 0 46 46" fill="none" stroke="var(--icon-line)" stroke-width="1.2">
          <circle cx="23" cy="23" r="21.5"/>
          <text x="23" y="21" text-anchor="middle" font-family="Georgia, serif" font-size="8" fill="var(--ink)" stroke="none">Made in</text>
          <text x="23" y="31" text-anchor="middle" font-family="Georgia, serif" font-size="8" font-weight="700" fill="var(--ink)" stroke="none">USA</text>
        </svg>
        <span>Proudly made in the USA</span>
      </li>
    </ul>

    <div class="count-badge">30 Packs</div>
    <div class="flavor-band">Velmo Plum Flavor</div>

    <svg class="sparkles" viewBox="0 0 190 150" fill="none" stroke="var(--brand-green)" stroke-width="2">
      <path d="M94 10 v26 M94 44 v26 M66 40 h24 M98 40 h24"/>
      <path d="M37 102 v16 M37 124 v16 M19 121 h15 M40 121 h15"/>
      <path d="M112 96 v8 M112 108 v8 M103 106 h7 M114 106 h7"/>
      <path d="M165 76 v9 M165 89 v9 M155 87 h8 M167 87 h8"/>
      <path d="M139 134 v5 M139 142 v5 M133 140 h5 M141 140 h5"/>
    </svg>
  </section>
</main>
</body>
</html>
```